Consulting firm need a professional powerpoint design

A startup Climate change firm needs a powerpoint template design. The design should reflect aspects of climate change adaptation, resilience and environmental sustainability.

The powerpoint design must convey aspects of nature and climate action for a resilient society.

The last slide of the powerpoint must have a allocation for a slogan such as 'Linking science and decision-making'.

Use the colors in the logo and business card for the powerpoint design.

Target Market(s)

Government and industry

Font styles to use
Sans Serif
Other font styles liked:
• nexa font family

Colors
85cae6
abd037
fece3e

Requirements
Must have
• - Colors used in logo and business card
- Convey science and nature
- Professional
Nice to have
• Many pages
Should not have
• Not complicated

```html
<!DOCTYPE html>
<html lang="en">
<head>
<meta charset="utf-8">
<title>Verdanova Presentation Template</title>
<link href="https://fonts.googleapis.com/css2?family=Montserrat:ital,wght@0,400;0,600;0,700;0,800;1,400&family=Jost:wght@300&display=swap" rel="stylesheet">
<style>
:root{
  --green:#abd037;
  --green-dark:#7fa33a;
  --yellow:#fece3e;
  --blue:#85cae6;
  --blue-deep:#2e86c1;
  --orange:#f39c34;
  --navy:#3a4156;
  --ink:#2f3550;
  --text:#3b3b3b;
  --band:#e4f3f9;
  --paper:#ffffff;
}
*{margin:0;padding:0;box-sizing:border-box}
html,body{width:720px;height:1200px;overflow:hidden;background:var(--paper)}
body{position:relative;font-family:"Montserrat",sans-serif;color:var(--text)}
.backdrop{position:absolute;inset:0}
.sheet-title{position:absolute;left:10px;top:4px;font-weight:800;font-size:24.5px;line-height:28.5px;color:var(--navy)}
.section-label{position:absolute;left:12px;font-family:"Jost",sans-serif;font-weight:300;font-size:15.5px;letter-spacing:10.2px;word-spacing:14px;color:var(--ink)}
.slide{position:absolute;width:160px;height:90px;background:var(--paper);box-shadow:2px 3px 5px rgba(0,0,0,.16);overflow:hidden}
.rule{position:absolute;height:.9px;background:linear-gradient(90deg,var(--orange) 0,var(--yellow) 32%,var(--blue-deep) 34%,var(--blue) 64%,#5aa537 66%,var(--green) 100%)}
.brand{position:absolute;display:flex;align-items:center;gap:2px;font-weight:700;font-size:4px;letter-spacing:.2px}
.brand i{display:block;width:5px;height:5px;border-radius:50%;background:var(--green)}
.cover-title{position:absolute;font-weight:700;font-size:8.3px;line-height:11.5px}
.sub{position:absolute;font-size:3px}
.s-title{position:absolute;left:8px;top:6px;font-weight:700;font-size:4.8px;color:var(--ink)}
.s-sub{position:absolute;left:8px;top:13px;font-size:2.2px;color:var(--text)}
.tx{position:absolute;font-size:2.3px;line-height:2.9px;color:var(--text)}
.tx b{display:block;font-weight:700}
.pg{position:absolute;right:7px;bottom:3px;width:6px;height:5px;border-radius:2px 0 2px 0;background:var(--green)}
.photo{position:absolute}
.quote-mark{position:absolute;font-weight:800;font-size:24px;line-height:1}
.q-text{position:absolute;font-style:italic;font-size:3.7px;line-height:5.4px}
.ring{position:absolute;width:48px;height:48px;border-radius:50%;border:4.5px solid var(--green);display:flex;align-items:center;justify-content:center;text-align:center;font-weight:700;font-size:3.3px;line-height:4px;color:var(--ink)}
.bubble{position:absolute;border-radius:50%;display:flex;align-items:center;justify-content:center;text-align:center;color:#fff;font-size:1.9px;line-height:2.4px;font-weight:700;padding:3px}
.petal{position:absolute;width:35px;height:35px;color:#fff;font-size:1.9px;line-height:2.4px;padding:20px 3px 0}
</style>
</head>
<body>
<svg class="backdrop" width="720" height="1200" aria-hidden="true"><polygon points="720,286 720,602 0,806 0,519" fill="var(--band)"/></svg>

<h1 class="sheet-title">Verdanova<br>Presentation<br>Template</h1>

<!-- Cover slides -->
<div class="section-label" style="top:116px">COVER SLIDES</div>

<div class="slide cover-a" style="left:9px;top:141px;background:var(--green)">
  <div style="position:absolute;left:0;top:0;width:160px;height:17px;background:var(--paper)"></div>
  <div class="brand" style="left:8px;top:6px;color:var(--navy)"><i></i>VERDANOVA</div>
  <div class="rule" style="left:0;top:17px;width:125px"></div>
  <div class="cover-title" style="left:8px;top:36px;color:#fff">Verdanova<br>Presentation<br>Template</div>
  <div class="sub" style="left:8px;top:73px;color:#fff">Please add sub-title here</div>
</div>

<div class="slide cover-b" style="left:190px;top:141px;background:var(--green)">
  <div class="brand" style="left:8px;top:9px;color:#fff"><i style="background:#fff"></i>VERDANOVA</div>
  <div class="photo" role="img" aria-label="White tree silhouette" style="right:0;top:0;width:72px;height:90px;border-radius:60% 0 0 40%;background:linear-gradient(160deg,rgba(255,255,255,.95),rgba(255,255,255,.75))"></div>
  <div class="cover-title" style="left:8px;top:34px;color:#fff">Verdanova<br>Presentation<br>Template</div>
  <div class="sub" style="left:8px;top:71px;color:#fff">Please add sub-title here</div>
</div>

<div class="slide cover-c" style="left:370px;top:141px">
  <div style="position:absolute;left:0;top:0;width:160px;height:20px;background:var(--navy)"></div>
  <div class="rule" style="left:0;top:21px;width:125px"></div>
  <div class="cover-title" style="left:8px;top:36px;color:var(--navy)">Verdanova<br>Presentation<br>Template</div>
  <div class="sub" style="left:8px;top:73px;color:var(--navy)">Please add sub-title here</div>
  <div class="brand" style="right:6px;bottom:7px;color:var(--navy)"><i></i>VERDANOVA</div>
</div>

<div class="slide cover-d" style="left:551px;top:141px">
  <div class="cover-title" style="left:8px;top:26px;color:var(--navy);line-height:10.5px">Verdanova Presentation<br>Template</div>
  <div class="rule" style="left:0;top:48px;width:124px"></div>
  <div class="brand" style="right:6px;bottom:7px;color:var(--navy)"><i></i>VERDANOVA</div>
</div>

<!-- Agenda slides -->
<div class="section-label" style="top:299px">AGENDA SLIDES</div>

<div class="slide agenda-a" style="left:9px;top:331px">
  <div class="photo" role="img" aria-label="Close-up photo of a green leaf with veins" style="left:0;top:0;width:160px;height:44px;background:linear-gradient(135deg,#4f8f2a,#8cc63f 55%,#5a9a2e)"></div>
  <div style="position:absolute;left:0;top:6px;width:40px;height:7px;background:rgba(255,255,255,.75)"></div>
  <div style="position:absolute;left:8px;top:6.5px;font-weight:700;font-size:5px;letter-spacing:.8px;color:var(--ink)">AGENDA</div>
  <div style="position:absolute;left:7px;top:44px;width:25px;height:2px;background:var(--blue)"></div>
  <div class="tx" style="left:8px;top:50px;width:24px;font-weight:700">ae ab illo inventore veritatis et</div>
  <div class="tx" style="left:38px;top:50px;width:24px">ae ab illo inventore veritatis et</div>
  <div class="tx" style="left:68px;top:50px;width:24px">ae ab illo inventore veritatis et</div>
  <div class="tx" style="left:98px;top:50px;width:24px">ae ab illo inventore veritatis et</div>
  <div class="tx" style="left:128px;top:50px;width:24px">ae ab illo inventore veritatis et</div>
  <div class="rule" style="left:0;bottom:0;width:160px"></div>
</div>

<div class="slide agenda-b" style="left:190px;top:331px">
  <div style="position:absolute;left:8px;top:7px;font-weight:700;font-size:5px;letter-spacing:.8px;color:var(--ink)">AGENDA</div>
  <div style="position:absolute;left:0;top:15px;width:53.3px;height:15px;background:var(--blue)"></div>
  <div style="position:absolute;left:53.3px;top:15px;width:53.4px;height:15px;background:var(--yellow)"></div>
  <div style="position:absolute;left:106.7px;top:15px;width:53.3px;height:15px;background:var(--green)"></div>
  <div class="tx" style="left:8px;top:47px;width:46px;font-weight:700">rem ipsum quia dolor sit amet, consectetur, adipisci</div>
  <div class="tx" style="left:61px;top:47px;width:46px">rem ipsum quia dolor sit amet, consectetur, adipisci</div>
  <div class="tx" style="left:114px;top:47px;width:46px">rem ipsum quia dolor sit amet, consectetur, adipisci</div>
</div>

<!-- Text heavy slides -->
<div class="section-label" style="top:488px">TEXT HEAVY SLIDES</div>

<div class="slide text-a" style="left:9px;top:513px">
  <div class="s-title">Please add slide title here</div>
  <div class="s-sub">Please add slide sub-title here</div>
  <div class="rule" style="left:8px;top:17px;width:145px"></div>
  <div class="tx" style="left:8px;top:22px;width:145px"><b>eaque ipsa quae ab illo inventore veritatis</b>"Sed ut perspiciatis unde omnis iste natus error sit voluptatem accusantium doloremque laudantium, totam rem aperiam, eaque ipsa quae ab illo inventore veritatis et quasi architecto beatae vitae dicta sunt explicabo. Nemo enim ipsam voluptatem quia voluptas sit aspernatur aut odit aut fugit, sed quia consequuntur magni dolores eos qui ratione voluptatem sequi nesciunt. Neque porro quisquam est, qui dolorem ipsum quia dolor sit amet, consectetur, adipisci velit, sed quia non numquam eius modi tempora incidunt ut labore et dolore magnam aliquam quaerat voluptatem. Ut enim ad minima veniam, quis nostrum exercitationem ullam corporis suscipit laboriosam, nisi ut aliquid ex ea commodi consequatur? Quis autem vel eum iure reprehenderit qui in ea voluptate velit esse quam nihil molestiae consequatur, vel illum qui dolorem eum fugiat quo voluptas nulla pariatur</div>
  <div class="pg"></div>
</div>

<div class="slide text-b" style="left:190px;top:513px">
  <div class="s-title">Please add slide title here</div>
  <div class="s-sub">Please add slide sub-title here</div>
  <div class="rule" style="left:8px;top:17px;width:145px"></div>
  <div class="tx" style="left:8px;top:22px;width:70px"><b>eaque ipsa quae ab illo inventore veritatis</b>"Sed ut perspiciatis unde omnis iste natus error sit voluptatem accusantium doloremque laudantium, totam rem aperiam, eaque ipsa quae ab illo inventore veritatis et quasi architecto beatae vitae dicta sunt explicabo. Nemo enim ipsam voluptatem quia voluptas sit aspernatur aut odit aut fugit, sed quia consequuntur magni dolores eos qui ratione voluptatem sequi nesciunt. Neque porro quisquam est, qui dolorem ipsum quia dolor sit amet, adipisci velit, sed quia non numquam eius modi tempora incidunt</div>
  <div class="tx" style="left:83px;top:22px;width:70px"><b>eaque ipsa quae ab illo inventore veritatis</b>ut labore et dolore magnam aliquam quaerat voluptatem. Ut enim ad minima veniam, quis nostrum exercitationem ullam corporis suscipit laboriosam, nisi ut aliquid ex ea commodi consequatur? Quis autem vel eum iure reprehenderit qui in ea voluptate velit esse quam nihil molestiae consequatur, vel illum qui dolorem eum fugiat quo voluptas nulla pariatur</div>
  <div class="pg"></div>
</div>

<div class="slide text-c" style="left:370px;top:513px">
  <div class="s-title">Please add slide title here</div>
  <div class="s-sub">Sub-title of the slide</div>
  <div class="rule" style="left:8px;top:17px;width:145px"></div>
  <div class="tx" style="left:8px;top:22px;width:46px"><b>eaque ipsa quae ab illo inventore veritatis</b>labore et dolore magnam aliquam quaerat voluptatem. Ut enim ad minima veniam, quis nostrum exercitationem ullam corporis suscipit laboriosam, nisi ut aliquid ex ea commodi consequatur? Quis autem vel eum iure reprehenderit qui in ea voluptate velit esse quam nihil molestiae consequatur, vel illum qui dolorem eum fugiat quo voluptas nulla pariatur</div>
  <div class="tx" style="left:58px;top:22px;width:46px"><b>eaque ipsa quae ab illo inventore veritatis</b>labore et dolore magnam aliquam quaerat voluptatem. Ut enim ad minima veniam, quis nostrum exercitationem ullam corporis suscipit laboriosam, nisi ut aliquid ex ea commodi consequatur? Quis autem vel eum iure reprehenderit qui in ea voluptate velit esse quam nihil molestiae consequatur, vel illum qui dolorem eum fugiat quo voluptas nulla pariatur</div>
  <div class="tx" style="left:108px;top:22px;width:46px"><b>eaque ipsa quae ab illo inventore veritatis</b>labore et dolore magnam aliquam quaerat voluptatem. Ut enim ad minima veniam, quis nostrum exercitationem ullam corporis suscipit laboriosam, nisi ut aliquid ex ea commodi consequatur? Quis autem vel eum iure reprehenderit qui in ea voluptate velit esse quam nihil molestiae consequatur, vel illum qui dolorem eum fugiat quo voluptas nulla pariatur</div>
  <div class="pg"></div>
</div>

<!-- Important slides -->
<div class="section-label" style="top:670px">IMPORTANT SLIDES</div>

<div class="slide quote-a" style="left:9px;top:695px">
  <div class="photo" role="img" aria-label="Faint line illustration of leaves growing from a light bulb" style="right:0;top:0;width:45px;height:60px;border-radius:50% 0 0 50%;background:linear-gradient(135deg,rgba(171,208,55,.22),rgba(171,208,55,.08))"></div>
  <div class="quote-mark" style="left:12px;top:18px;color:var(--green)">“</div>
  <div class="q-text" style="left:30px;top:30px;width:118px;color:var(--ink)">Perspiciatis unde omnis iste natus error sit voluptatem accusantium doloremque, totam rem aperiam, eaque ipsa quae ab illo inventore veritatis et quasi architecto beatae vitae dicta sunt explicabo. Nemo enim ipsam voluptatem quia voluptas sit aspernatur aut odit aut fugit, sed quia consequuntur magni.</div>
  <div class="rule" style="left:0;bottom:0;width:160px"></div>
</div>

<div class="slide quote-b" style="left:190px;top:695px">
  <div class="s-title">Please add slide title here</div>
  <div class="tx" style="left:8px;top:22px;width:68px">ut labore et dolore magnam aliquam quaerat voluptatem. Ut enim ad minima veniam, quis nostrum exercitationem ullam corporis labore et dolore magnam aliquam quaerat voluptatem. Ut enim ad minima veniam, quis nostrum exercitationem ullam corporis suscipit laboriosam, nisi ut aliquid ex ea commodi consequatur s suscipit laboriosam, nisi ut aliquid ex ea commodi consequatur?</div>
  <div style="position:absolute;left:80px;top:0;width:80px;height:90px;background:var(--yellow)"></div>
  <div class="quote-mark" style="left:84px;top:10px;color:var(--ink)">“</div>
  <div class="q-text" style="left:101px;top:21px;width:54px;font-size:3.6px;line-height:5.2px;color:var(--ink)">ut labore et dolore magnam aliquam quaerat voluptatem. Ut enim ad minima veniam, quis nostrum exercitationem ullam corporis suscipit laboriosam, nisi ut aliquid ex ea commodi consequatur?</div>
</div>

<div class="slide heading-blob" style="left:370px;top:695px">
  <svg style="position:absolute;left:0;top:0" width="160" height="90" aria-hidden="true"><path d="M25 13 C45 8 60 20 64 34 C68 48 80 52 80 66 C80 80 66 85 58 78 C50 72 44 68 30 68 C14 68 6 56 6 40 C6 24 12 16 25 13Z" fill="var(--blue)"/></svg>
  <div style="position:absolute;left:15px;top:25px;font-weight:600;font-size:6px;line-height:8.8px;color:#fff">Important<br>heading<br>please</div>
  <div class="tx" style="left:72px;top:11px;width:60px">Sed ut perspiciatis unde omnis iste natus error sit voluptatem accusantium doloremque laudantium, totam rem aperiam, eaque ipsa quae ab illo inventore veritatis et quasi architecto beatae vitae dicta sunt explicabo. Nemo enim ipsam voluptatem quia voluptas sit aspernatur aut odit aut fugit, sed quia consequuntur magni dolores eos qui ratione voluptatem sequi nesciunt. Neque porro quisquam est.</div>
  <div class="photo" role="img" aria-label="Light blue wind turbines illustration" style="right:0;top:4px;width:34px;height:86px;background:linear-gradient(180deg,rgba(133,202,230,.45),rgba(133,202,230,.15))"></div>
  <div class="rule" style="left:0;bottom:0;width:160px"></div>
</div>

<div class="slide chart-slide" style="left:551px;top:695px">
  <div class="s-title" style="font-size:4.6px">Topic of the slide</div>
  <div class="s-sub">Any sub title here please</div>
  <div class="rule" style="left:8px;top:17px;width:145px"></div>
  <div class="tx" style="left:8px;top:21px;font-weight:700">Your Chart title Here Please</div>
  <div class="tx" style="left:82px;top:21px;font-weight:700">Your Chart title Here Please</div>
  <svg style="position:absolute;left:0;top:0" width="160" height="90" aria-hidden="true">
    <g fill="none" stroke-width="2.4">
      <circle cx="28" cy="53" r="10" stroke="var(--blue)"/>
      <circle cx="28" cy="53" r="10" stroke="var(--yellow)" stroke-dasharray="22 100" transform="rotate(-90 28 53)"/>
      <circle cx="28" cy="53" r="10" stroke="#5aa537" stroke-dasharray="0 22 8 100" transform="rotate(-90 28 53)"/>
      <circle cx="62" cy="53" r="10" stroke="var(--blue)"/>
      <circle cx="62" cy="53" r="10" stroke="var(--green)" stroke-dasharray="26 100" transform="rotate(-90 62 53)"/>
      <circle cx="62" cy="53" r="10" stroke="var(--yellow)" stroke-dasharray="0 26 6 100" transform="rotate(-90 62 53)"/>
    </g>
    <text x="28" y="54" font-size="2.2" text-anchor="middle" font-family="Montserrat, sans-serif" fill="#333">Pie 01</text>
    <text x="62" y="54" font-size="2.2" text-anchor="middle" font-family="Montserrat, sans-serif" fill="#333">Pie 02</text>
    <g>
      <rect x="84" y="40" width="2.4" height="28" fill="var(--blue)"/><rect x="87" y="52" width="2.4" height="16" fill="var(--green)"/><rect x="90" y="56" width="2.4" height="12" fill="var(--yellow)"/>
      <rect x="102" y="52" width="2.4" height="16" fill="var(--blue)"/><rect x="105" y="38" width="2.4" height="30" fill="var(--green)"/><rect x="108" y="54" width="2.4" height="14" fill="var(--yellow)"/>
      <rect x="120" y="46" width="2.4" height="22" fill="var(--blue)"/><rect x="123" y="58" width="2.4" height="10" fill="var(--green)"/><rect x="126" y="51" width="2.4" height="17" fill="var(--yellow)"/>
      <rect x="138" y="46" width="2.4" height="22" fill="var(--blue)"/><rect x="141" y="44" width="2.4" height="24" fill="var(--green)"/><rect x="144" y="34" width="2.4" height="34" fill="var(--yellow)"/>
    </g>
    <g font-size="1.9" font-family="Montserrat, sans-serif" fill="#333" text-anchor="middle">
      <text x="88" y="72">Category 1</text><text x="106" y="72">Category 2</text><text x="124" y="72">Category 3</text><text x="142" y="72">Category 4</text>
    </g>
  </svg>
  <div class="pg"></div>
</div>

<div class="slide section-a" style="left:9px;top:808px;background:var(--green)">
  <div class="photo" role="img" aria-label="Pale line illustration of leaves growing from a light bulb" style="right:0;top:0;width:48px;height:90px;border-radius:50% 0 0 30%;background:linear-gradient(180deg,rgba(255,255,255,.35),rgba(255,255,255,.2))"></div>
  <div style="position:absolute;left:8px;top:68px;font-weight:700;font-size:9.5px;color:#fff">Section break</div>
</div>

<div class="slide section-b" style="left:187px;top:808px;background:var(--blue)">
  <div class="photo" role="img" aria-label="Blue line illustration of leaves growing from a light bulb" style="right:0;top:4px;width:56px;height:58px;border-radius:50% 0 0 50%;background:linear-gradient(135deg,rgba(46,134,193,.55),rgba(46,134,193,.25))"></div>
  <div style="position:absolute;left:30px;top:41px;font-weight:600;font-size:6.8px;line-height:9.8px;color:#fff">Section break slide<br>sub-heading here please</div>
  <div class="sub" style="left:30px;top:63px;font-size:2.2px;color:#fff">Section break slide sub-heading here please</div>
</div>

<!-- Infographics and photos -->
<div class="section-label" style="top:963px">INFOGRAPHICS AND PHOTOS</div>

<div class="slide info-bubbles" style="left:9px;top:990px">
  <div class="photo" role="img" aria-label="Lavender illustration of an open hand" style="left:55px;top:62px;width:55px;height:28px;border-radius:40% 60% 0 0;background:linear-gradient(160deg,#c7cbe6,#aeb4da)"></div>
  <div class="bubble" style="left:51px;top:5px;width:23px;height:23px;background:var(--yellow)">inventore veritatis et quasi beatae vitae</div>
  <div class="bubble" style="left:20px;top:17px;width:32px;height:32px;background:var(--blue)">inventore veritatis et quasi architecto beatae vitae dicta sunt</div>
  <div class="bubble" style="left:62px;top:26px;width:33px;height:33px;background:var(--green)">inventore veritatis et quasi architecto beatae vitae dicta sunt</div>
  <div class="bubble" style="left:113px;top:40px;width:22px;height:22px;background:#fde08a;color:var(--ink)">inventore veritatis et quasi</div>
  <div class="bubble" style="left:38px;top:54px;width:24px;height:24px;background:#d8e8a8;color:var(--ink)">inventore veritatis et quasi architecto</div>
  <div style="position:absolute;left:89px;top:14px;font-weight:600;font-size:6px;line-height:8.5px;color:var(--ink)">Short title<br>here please</div>
  <div class="pg"></div>
</div>

<div class="slide info-petals" style="left:187px;top:990px">
  <div style="position:absolute;left:7px;top:30px;font-weight:600;font-size:6px;line-height:8.5px;color:var(--ink)">Title for this<br>slide here<br>please</div>
  <div style="position:absolute;left:67px;top:9px;width:5px;height:5px;border-radius:3px 0;background:var(--green)"></div>
  <div class="petal" style="left:76px;top:10px;border-radius:14px 0 14px 0;background:var(--yellow)">inventore veritatis et quasi architecto beatae</div>
  <div class="petal" style="left:113px;top:10px;border-radius:0 14px 0 14px;background:var(--blue)">inventore veritatis et quasi architecto beatae</div>
  <div class="petal" style="left:76px;top:47px;border-radius:0 14px 0 14px;background:var(--green-dark)">inventore veritatis et quasi architecto beatae</div>
  <div class="petal" style="left:113px;top:47px;border-radius:14px 0 14px 0;background:var(--green)">inventore veritatis et quasi architecto beatae</div>
  <div style="position:absolute;left:148px;top:76px;width:5px;height:5px;border-radius:3px 0;background:var(--green)"></div>
  <div class="pg"></div>
</div>

<div class="slide info-rings" style="left:365px;top:990px">
  <div class="s-title" style="font-size:4.6px">Please add your title here</div>
  <div class="rule" style="left:8px;top:17px;width:145px"></div>
  <div class="ring" style="left:7px;top:22px">This is just<br>placeholder<br>text only.</div>
  <div class="ring" style="left:55px;top:22px">This is just<br>placeholder<br>text only.</div>
  <div class="ring" style="left:103px;top:22px">This is just<br>placeholder<br>text only.</div>
  <div class="pg"></div>
</div>

<div class="slide info-navy" style="left:545px;top:990px">
  <div style="position:absolute;left:7px;top:18px;width:72px;font-weight:600;font-size:6.4px;line-height:8.4px;color:var(--ink)">Sed ut perspiciatis unde omnis iste natus</div>
  <div style="position:absolute;left:7px;top:48px;width:72px;font-size:3.6px;line-height:5.2px;color:var(--ink)">Sed ut perspiciatis unde omnis iste natus error sit voluptatem accusantium doloremque laudantium</div>
  <div style="position:absolute;left:80px;top:0;width:80px;height:90px;background:var(--navy)"></div>
  <div class="photo" role="img" aria-label="White line illustration of leaves growing from a light bulb" style="left:90px;top:6px;width:50px;height:78px;border-radius:45% 45% 20% 20%;background:linear-gradient(180deg,rgba(255,255,255,.28),rgba(255,255,255,.12))"></div>
</div>

<div class="slide photo-fern" style="left:9px;top:1100px">
  <div style="position:absolute;left:0;top:0;width:55px;height:90px;background:var(--green)"></div>
  <div style="position:absolute;left:7px;top:16px;font-weight:600;font-size:6.6px;line-height:9.6px;color:#fff">Please add<br>title for slide<br>here</div>
  <div class="photo" role="img" aria-label="Photo of dark green fern fronds" style="left:56px;top:0;width:104px;height:90px;background:radial-gradient(circle at 45% 45%,#2f6b3a,#143a20 60%,#0b2414)"></div>
</div>

<div class="slide photo-sky" style="left:190px;top:1100px">
  <div class="s-title" style="font-size:4.6px">Please add topic title here</div>
  <div class="tx" style="left:8px;top:22px;width:66px">Sed ut perspiciatis unde omnis iste natus error sit voluptatem accusantium doloremque laudantium, totam rem aperiam, eaque ipsa quae ab illo inventore veritatis et quasi architecto beatae vitae dicta sunt explicabo. Nemo enim ipsam voluptatem quia voluptas sit aspernatur aut odit aut fugit, sed quia consequuntur magni dolores eos qui ratione voluptatem sequi nesciunt. Neque porro quisquam est.</div>
  <div class="photo" role="img" aria-label="Photo of a wind turbine on a grassy hill under a blue sky with clouds" style="left:80px;top:0;width:80px;height:90px;background:linear-gradient(180deg,#2f86c8 0,#8cc3e8 45%,#d9e9f2 62%,#b7a84a 72%,#8a8a35 100%)"></div>
</div>

<div class="slide closing" style="left:370px;top:1100px">
  <div style="position:absolute;left:8px;top:64px;font-weight:800;font-size:8px;line-height:10.4px;color:var(--navy)">Linking science<br>&amp; decision-making</div>
</div>
</body>
</html>
```